Recruitment Ad for Social Media Marketing

Ad used to recruit Mortgage Originators

Target Market(s)

Real Estate Agents

Colors

Designer to choose colors to be used in the design.

Requirements
Must have
• REALTORS
• If you can send a text message, you can earn Mortgage Originator Income too...
• at Bluegate Lending Partners, "If you open the Bluegate, We'll handle the rest"
• We reimburse 100% of Licensing Costs
• * Immediate Payouts
• * Up to 75% Commission Split
• * No Goals or Quotas
• * Manage Your Own Schedule
• * Work from Home
• Send Resume to Employment@bluegatelendhub.com
• Bluegate Lending Partners, Inc.
• 7200 Marlowe Lane, Ellicott City, MD 21046
• (800) 641-2907 Ext. 23
• NMLS #318760
• (SMALL PRINT AT BOTTOM)
• **Dual income requirements governed by state law. In most cases, Realtors cannot serve in a dual capacity for the same transaction.

```html
<!DOCTYPE html>
<html lang="en">
<head>
<meta charset="utf-8">
<title>Bluegate Lending Partners – Recruitment Flyer</title>
<link href="https://fonts.googleapis.com/css2?family=Lato:wght@400;700;900&family=Barlow:wght@700;800&display=swap" rel="stylesheet">
<style>
  :root {
    --backdrop: #e9e4e1;
    --paper: #ffffff;
    --royal: #0b5ea8;
    --royal-light: #1f7cc4;
    --royal-dark: #0a4f94;
    --band: #3a63b3;
    --olive: #a89b32;
    --gold: #d2ab2e;
    --frame: #eceeef;
    --ink-blue: #0c4f9a;
    --photo-warm: #c9a27f;
    --photo-cool: #e8e2da;
  }
  * { margin: 0; padding: 0; box-sizing: border-box; }
  html, body { width: 1200px; height: 960px; overflow: hidden; }
  body { background: var(--backdrop); font-family: "Lato", sans-serif; }

  .flyer {
    position: absolute; left: 255px; top: 30px;
    width: 690px; height: 900px;
    background: var(--paper);
    box-shadow: 0 10px 30px rgba(0,0,0,.18);
    overflow: hidden;
  }
  .flyer-shapes { position: absolute; inset: 0; }

  .photo {
    position: absolute; left: 40px; top: 150px; width: 395px; height: 410px;
    clip-path: polygon(0 12%, 100% 0, 100% 100%, 0 100%);
    background: linear-gradient(135deg, var(--photo-warm), var(--photo-cool) 70%);
  }

  .kicker {
    position: absolute; left: 36px; top: 20px;
    color: #fff; font-weight: 900; font-size: 14px; letter-spacing: 3px;
  }
  .headline {
    position: absolute; left: 36px; top: 42px;
    color: #fff; font-weight: 900; font-size: 27px; line-height: 1.12;
  }

  .pitch {
    position: absolute; right: 26px; top: 56px; width: 220px;
    text-align: right; color: #fff; font-weight: 700; font-size: 16px; line-height: 1.3;
  }

  .offer {
    position: absolute; right: 26px; top: 250px; width: 250px;
    text-align: right; color: #fff; font-family: "Barlow", sans-serif;
    font-weight: 800; text-transform: uppercase; line-height: 1;
  }
  .offer-small { font-size: 32px; }
  .offer-big { font-size: 92px; letter-spacing: -2px; margin: 2px 0 0; }

  .perks {
    position: absolute; left: 56px; top: 600px;
    list-style: none; color: var(--ink-blue);
    font-weight: 700; font-size: 18px; line-height: 1.28;
  }
  .perks li::before { content: "•"; margin-right: 10px; }

  .phone-block {
    position: absolute; left: 48px; top: 720px; width: 270px;
    border-top: 3px solid var(--ink-blue);
    padding-top: 4px;
    color: var(--ink-blue);
  }
  .phone { font-weight: 900; font-size: 24px; line-height: 1.1; white-space: nowrap; }
  .nmls { text-align: right; font-weight: 900; font-size: 12px; }

  .brand {
    position: absolute; left: 470px; top: 620px; width: 200px;
    display: flex; align-items: center; gap: 10px;
  }
  .brand-dot { width: 34px; height: 34px; border-radius: 50%; background: var(--gold); flex: none; }
  .brand-name { font-weight: 900; font-size: 19px; line-height: 1.15; color: var(--ink-blue); }

  .company {
    position: absolute; right: 24px; top: 776px; text-align: right; color: #fff;
  }
  .company-name { font-weight: 900; font-size: 16px; }
  .company-address { font-size: 14px; margin-top: 2px; }

  .resume {
    position: absolute; left: 48px; top: 830px; color: #fff;
  }
  .resume-label { font-weight: 900; font-size: 15px; text-transform: uppercase; }
  .resume-email { font-size: 15px; }

  .small-print {
    position: absolute; left: 24px; right: 24px; bottom: 6px;
    color: #fff; font-size: 9px; text-align: center; opacity: .9;
  }
</style>
</head>
<body>
  <main class="flyer">
    <svg class="flyer-shapes" viewBox="0 0 690 900" width="690" height="900" aria-hidden="true">
      <polygon points="440,0 690,0 690,515 435,555" fill="var(--olive)"/>
      <polygon points="435,555 690,515 690,535 450,600" fill="var(--gold)"/>
      <polygon points="380,0 470,0 330,150 300,150" fill="var(--royal-light)"/>
      <polygon points="0,0 450,0 300,140 40,205 0,175" fill="var(--royal)"/>
      <polygon points="28,562 438,545 438,568 34,590" fill="var(--frame)"/>
      <polygon points="0,818 690,728 690,900 0,900" fill="var(--band)"/>
      <polygon points="0,818 360,771 360,781 0,830" fill="var(--royal-dark)"/>
    </svg>

    <div class="photo" role="img" aria-label="Photo of two smiling professionals seated at a meeting"></div>

    <p class="kicker">REALTORS</p>
    <h1 class="headline">If You Open The Bluegate,<br>We'll Handle<br>The Rest</h1>

    <p class="pitch">If you can send a text message, you can earn Mortgage Originator Income too...</p>

    <div class="offer">
      <div class="offer-small">We</div>
      <div class="offer-small">Reimburse</div>
      <div class="offer-big">100%</div>
      <div class="offer-small">of Licensing</div>
      <div class="offer-small">Costs</div>
    </div>

    <div class="brand">
      <span class="brand-dot"></span>
      <span class="brand-name">Bluegate Lending Partners, Inc.</span>
    </div>

    <ul class="perks">
      <li>Immediate Payouts</li>
      <li>Up to 75% Commission Split</li>
      <li>No Goals or Quotas</li>
      <li>Manage Your Own Schedule</li>
      <li>Work from Home</li>
    </ul>

    <div class="phone-block">
      <div class="phone">(800) 641-2907 Ext. 23</div>
      <div class="nmls">NMLS #318760</div>
    </div>

    <div class="company">
      <div class="company-name">Bluegate Lending Partners, Inc.</div>
      <div class="company-address">7200 Marlowe Lane, Ellicott City, MD 21046</div>
    </div>

    <div class="resume">
      <div class="resume-label">Send Resume:</div>
      <div class="resume-email">Employment@bluegatelendhub.com</div>
    </div>

    <p class="small-print">**Dual income requirements governed by state law. In most cases, Realtors cannot serve in a dual capacity for the same transaction.</p>
  </main>
</body>
</html>
```